Card Design for my dog training business Rustpaw Obedience

Need a business card design for my dog training business with my new logo. Want the card to come off professional yet fun. Want it to be very eye catchy as well. I normally have these at vet clinics, pet stores, and groomers. so need it to look better than my competitors.
Target Market(s)
dog owners
Industry/Entity Type
Dog Training
Contact Information for Business Card
needs logo, my name and info
Font styles to use
Serif
Colors
0255a3
ffffff
ec1f27
000000
333333
fbfbfb
Requirements
Must have
- Rustpaw Obedience
- Hollis Brandt
- 415 903 2267
- info@rustpawobedience.example
- www.rustpawobedience.example

```html
<!DOCTYPE html>
<html lang="en">
<head>
<meta charset="utf-8">
<title>Rustpaw Obedience — Business Card</title>
<link rel="stylesheet" href="https://fonts.googleapis.com/css2?family=Libre+Baskerville:wght@400&display=swap">
<style>
  :root {
    --stage: #3a3b3d;
    --card-blue: #045a80;
    --card-white: #ffffff;
    --ink: #1f1f1f;
    --accent-blue: #1d6c94;
    --faint: #d4d4d4;
    --on-blue: #ffffff;
  }
  html, body {
    margin: 0;
    width: 1200px;
    height: 900px;
    overflow: hidden;
    background: var(--stage);
    font-family: "Libre Baskerville", Georgia, serif;
  }
  .canvas {
    position: relative;
    width: 1200px;
    height: 900px;
  }
  .card {
    position: absolute;
    width: 525px;
    height: 300px;
    box-shadow: 0 14px 30px rgba(0,0,0,0.45);
  }
  /* Front */
  .card-front {
    left: 90px;
    top: 100px;
    background: var(--card-blue);
    color: var(--on-blue);
  }
  .card-front .brand {
    position: absolute;
    left: 0; right: 0;
    top: 96px;
    text-align: center;
    font-size: 24px;
    line-height: 1.25;
    letter-spacing: 0.02em;
  }
  .card-front .website {
    position: absolute;
    left: 0; right: 0;
    bottom: 48px;
    text-align: center;
    font-size: 12px;
    letter-spacing: 0.02em;
  }
  /* Back */
  .card-back {
    left: 585px;
    top: 480px;
    background: var(--card-white);
    color: var(--ink);
  }
  .card-back .brand-mark {
    position: absolute;
    left: 150px;
    top: 92px;
    width: 260px;
    text-align: center;
    font-size: 30px;
    line-height: 1.2;
    color: var(--faint);
  }
  .card-back .person {
    position: absolute;
    left: 32px;
    top: 48px;
  }
  .card-back .person-name {
    margin: 0;
    font-size: 15px;
    color: var(--accent-blue);
    letter-spacing: 0.02em;
  }
  .card-back .person-role {
    margin: 4px 0 0 12px;
    font-size: 11px;
  }
  .card-back .contact {
    position: absolute;
    left: 32px;
    bottom: 30px;
    font-size: 13px;
    line-height: 1.5;
  }
  .card-back .website-vertical {
    position: absolute;
    right: 18px;
    top: 20px;
    writing-mode: vertical-rl;
    font-size: 12px;
    letter-spacing: 0.02em;
  }
</style>
</head>
<body>
  <main class="canvas">
    <section class="card card-front" aria-label="Card front">
      <div class="brand">Rustpaw<br>Obedience</div>
      <div class="website">www.rustpawobedience.example</div>
    </section>

    <section class="card card-back" aria-label="Card back">
      <div class="brand-mark" aria-hidden="true">Rustpaw<br>Obedience</div>
      <div class="person">
        <p class="person-name">HOLLIS BRANDT</p>
        <p class="person-role">Owner</p>
      </div>
      <div class="contact">
        <div class="phone">415 903 2267</div>
        <div class="email">info@rustpawobedience.example</div>
      </div>
      <div class="website-vertical">www.rustpawobedience.example</div>
    </section>
  </main>
</body>
</html>
```